Website Design for Gifts and Souvenirs online store PSD only

I need designs of homepage, product page, product list page and category page for "web store" PSD files only. Website will be using magento engine.

For more information please see [login to view URL]

I have 2 logos ready one of them will be used for design please use attached logos( logo1 is prefered).

I hope to complete this within 5-10 days, so if I get a great design in the next few days, I will chose winner before the contest ends.

What the Site Will Do
The Petal Parcels website will be selling Russian Souvenirs in the USA market as the main line of the products it will heavily advertise through Chatterleaf for the Russian community in the USA. Our Russian product lines customer base is very wide from 20 years old men and women and up, but main customer’s base are women 40-60 years old. These souvenirs will be imported from Russia and sold online in USA.
The second part of our website will be dedicated to Religious products. We will carry many Icons, Easter eggs and crucifixions for people who follow Christian Orthodox Church doctrines. These people are mainly Russians and the products that we sell for them will be made in Russia too. We also will be selling a lot of religious figurines that represent Christian Catholics world view and are different from Christian Orthodoxism.
The third part of our website will be selling figurines of all kind mostly coming from China. Those figurines will be made from glass porcelain stone, polystone wood and gyps. The main customers for these products are Americans 16 years and up. The traffic for these products should come from our BidNook sales where in packages that we sell promotion flyer will be included with the discount codes to use on our website on future purchases.

I like following websites

Navigation
Product categories, Shopping cart Registration for new user, Login for existing, Basic search, About US/contact US, Customer service, Site map, Orders and Returns
Chatterleaf Snapmira chirpel clipvane and Q+ buttons. please make them clear and everyone can see.

Logo
Logo 1 is preferable but can be done with logo 2 as well.

Colors
For colors please try to match them to logo colors but i like bright and light colors.

The final design should be provided in an Adobe Photoshop .PSD format files and should have well named layers. The design should be large enough to fill the width of an HD monitor (1920px) without having large margins.

I've uploaded file with some of the products that will be selling on the website.

```html
<!DOCTYPE html>
<html lang="en">
<head>
<meta charset="utf-8">
<title>Petal Parcels — Home</title>
<link rel="stylesheet" href="https://fonts.googleapis.com/css2?family=Open+Sans:wght@400;600;700;800&family=Yeseva+One&display=swap">
<style>
:root{
  --red:#e8312f;
  --red-dark:#c9201f;
  --ink:#1c1c1c;
  --text:#3a3a3a;
  --muted:#8a8a8a;
  --navy:#24303a;
  --kids:#5ab4e5;
  --girls:#e0177a;
  --boys:#147ab8;
  --other:#ef5a0d;
  --footer-bar:#2b2b2b;
  --white:#ffffff;
}
*{box-sizing:border-box;margin:0;padding:0}
html,body{width:1200px;height:2612px;overflow:hidden;background:var(--white)}
body{position:relative;font-family:"Open Sans",Arial,sans-serif;color:var(--text)}
.abs{position:absolute}

/* header */
.brand{left:128px;top:16px;width:150px;display:flex;flex-direction:column;align-items:center;gap:6px}
.brand-dot{width:30px;height:30px;border-radius:50%;background:var(--red)}
.brand-name{font-size:20px;font-weight:700;color:var(--red);line-height:24px;white-space:nowrap}
.search{left:303px;top:37px;width:342px;height:34px;border:2px solid var(--navy);border-radius:18px;display:flex;overflow:hidden}
.search-cat{background:var(--navy);color:#fff;font-size:11px;width:121px;display:flex;align-items:center;justify-content:center;gap:4px}
.search-field{flex:1;position:relative}
.search-field svg{position:absolute;right:12px;top:8px}
.utility{top:14px;font-size:11px;color:var(--muted)}
.nav-link{top:46px;font-size:13px;color:#555}
.signup{left:939px;top:41px;width:112px;height:26px;background:var(--red);color:#fff;font-size:12px;display:flex;align-items:center;justify-content:center}

/* hero */
.hero{left:37px;top:104px;width:1124px;height:425px;background:radial-gradient(circle at 40% 35%,#6fb8a8 0,#3d8f96 22%,transparent 40%),radial-gradient(circle at 78% 60%,#c7b79f 0,#8e9a8c 20%,transparent 38%),linear-gradient(100deg,#e8a35b 0%,#d9924f 25%,#5d9b9a 55%,#6f7f78 80%,#7a8a86 100%)}
.cat-panel{left:51px;top:120px;width:212px;height:396px;background:#fff;padding:14px 22px}
.cat-panel h2{font-weight:400;font-size:20px;color:#666;text-align:center;margin-bottom:10px}
.cat-panel li{list-style:none;font-size:14.5px;color:#888;line-height:27px}
.cat-panel .all{color:var(--red);font-size:13px;margin-top:6px;text-align:center}
.promo{left:767px;top:222px;width:266px;height:170px;background:#f04e55;transform:rotate(-4deg);display:flex;flex-direction:column;align-items:center;justify-content:center;font-family:"Yeseva One",serif;color:#fff}
.promo .big{font-size:34px;line-height:44px}
.promo-tag{left:808px;top:355px;width:230px;height:44px;background:#5b3a76;transform:rotate(-8deg);color:#fff;font-family:"Yeseva One",serif;font-size:22px;display:flex;align-items:center;justify-content:center}
.hero-arrows{left:1091px;top:273px;width:44px;height:83px;background:#fff;border-radius:22px}
.hero-dots{left:1053px;top:495px;display:flex;gap:4px}
.hero-dots i{width:16px;height:16px;border-radius:50%;background:#fff}

/* sections */
.rule{height:12px;border-top:6px solid var(--ink);border-bottom:2px solid var(--ink)}
.circle-btn{width:44px;height:44px;border:2px solid var(--ink);border-radius:50%;display:flex;align-items:center;justify-content:center}
.circle-btn.sm{width:24px;height:24px}
.section-title{font-weight:800;color:var(--red);font-size:25px;text-align:center;letter-spacing:.3px}

.tile{display:flex;align-items:flex-end;justify-content:center;padding-bottom:12px;color:#fff;font-size:19px;font-weight:600;text-shadow:0 1px 3px rgba(0,0,0,.5)}

.gift-for{top:1411px;width:256px;height:102px;color:#fff;font-weight:800;font-size:25px;letter-spacing:1px;display:flex;align-items:center;justify-content:center}

.price{position:absolute;left:0;bottom:0;width:72px;height:72px;border-radius:0 36px 0 0;background:rgba(36,48,58,.75);color:#fff;font-size:25px;display:flex;align-items:center;justify-content:center}
.price.sm{width:56px;height:44px;border-radius:0 22px 0 0;font-size:18px}
.caption{font-size:17px;color:#333;white-space:nowrap}

/* snapmira strip */
.strip{left:0;top:2179px;width:1200px;height:166px;display:flex}
.strip > div{height:100%}
.follow-box{left:169px;top:2167px;width:180px;height:178px;background:var(--navy);color:#fff;padding:22px 20px}
.follow-box h3{font-size:21px;font-weight:700;line-height:26px}
.follow-btn{margin-top:14px;width:136px;height:34px;background:#2f4150;display:flex;align-items:center;justify-content:space-between;padding:0 12px;font-weight:700;font-size:17px;color:#cfe3f1}

/* footer */
.foot-h{top:2376px;font-size:13px;font-weight:700;color:#222}
.foot-list{top:2400px;font-size:11.5px;line-height:18.5px;color:#444;list-style:none}
.about-text{left:75px;top:2402px;width:215px;font-size:8.5px;line-height:12.5px;color:#333}
.about-btn{left:73px;top:2488px;width:108px;height:32px;border:2px solid var(--red);padding:2px}
.about-btn span{display:flex;width:100%;height:100%;background:var(--red);color:#fff;font-size:12px;align-items:center;justify-content:center}
.social{left:763px;top:2400px;list-style:none;font-size:11.5px;color:#444;line-height:18.5px}
.social li{display:flex;align-items:center;gap:7px}
.social li::before{content:"";width:11px;height:11px;border-radius:50%;background:var(--red)}
.email{left:951px;top:2400px;width:165px;height:47px;border:2px solid #333;font-size:12px;color:#999;padding:14px 8px}
.subscribe{left:951px;top:2453px;width:98px;height:34px;background:var(--red);color:#fff;font-size:12px;font-weight:700;display:flex;align-items:center;justify-content:center}
.bottom-bar{left:0;top:2571px;width:1200px;height:41px;background:var(--footer-bar);color:#ddd;font-size:11px;display:flex;align-items:center;justify-content:center}
</style>
</head>
<body>

<!-- header -->
<div class="abs brand"><span class="brand-dot"></span><span class="brand-name">Petal Parcels</span></div>
<div class="abs search">
  <div class="search-cat">All Categories <svg width="8" height="6" viewBox="0 0 8 6"><path d="M1 1l3 3 3-3" stroke="#fff" stroke-width="1.5" fill="none"/></svg></div>
  <div class="search-field"><svg width="16" height="16" viewBox="0 0 16 16"><circle cx="6.5" cy="6.5" r="4.5" stroke="#8aa" stroke-width="2" fill="none"/><path d="M10 10l4 4" stroke="#8aa" stroke-width="2"/></svg></div>
</div>
<div class="abs utility" style="left:873px">My Account ▾</div>
<div class="abs utility" style="left:973px;display:flex;gap:6px;align-items:center">
  <svg width="18" height="14" viewBox="0 0 18 14"><path d="M1 1h3l2 8h9l2-6H5" stroke="var(--red)" stroke-width="1.6" fill="none"/><circle cx="7" cy="12" r="1.3" fill="var(--red)"/><circle cx="14" cy="12" r="1.3" fill="var(--red)"/></svg>0 Items ▾
</div>
<div class="abs nav-link" style="left:759px">About Us</div>
<div class="abs nav-link" style="left:844px">Contact Us</div>
<div class="abs signup">Sign Up / Login</div>

<!-- hero -->
<div class="abs hero" role="img" aria-label="Colourful toy balls with rainbow and gem prints on a warm background"></div>
<nav class="abs cat-panel">
  <h2>Categories</h2>
  <ul>
    <li>Angels &amp; Religious</li><li>Animals</li><li>Animated Characters</li><li>Baby's First Christmas</li>
    <li>Children &amp; Family</li><li>Holiday Accents</li><li>Ornament Tree Sets</li><li>Santas &amp; Trees</li>
    <li>Snowflakes &amp; Snowmen</li><li>Wedding</li><li>Animals</li>
  </ul>
  <div class="all">All Categories ›</div>
</nav>
<div class="abs promo"><span class="big">Play or</span><span class="big">Showcase</span></div>
<div class="abs promo-tag">Shop Now</div>
<div class="abs hero-arrows"><svg width="44" height="83" viewBox="0 0 44 83"><path d="M26 20l-9 10 9 10M18 43l9 10-9 10" stroke="var(--red)" stroke-width="4" fill="none" stroke-linecap="round"/></svg></div>
<div class="abs hero-dots"><i></i><i></i><i></i><i></i></div>

<!-- trending -->
<div class="abs circle-btn" style="left:130px;top:555px"><svg width="14" height="14" viewBox="0 0 14 14"><path d="M9 2L4 7l5 5" stroke="var(--red)" stroke-width="2.5" fill="none"/></svg></div>
<div class="abs rule" style="left:235px;top:571px;width:720px"></div>
<div class="abs circle-btn" style="left:1015px;top:555px"><svg width="14" height="14" viewBox="0 0 14 14"><path d="M5 2l5 5-5 5" stroke="var(--red)" stroke-width="2.5" fill="none"/></svg></div>
<h2 class="abs section-title" style="left:0;width:1248px;top:612px">SEE WHATS TRENDING</h2>

<div class="abs tile" style="left:73px;top:691px;width:175px;height:173px;background:linear-gradient(#f1ece0,#b8ad95)" role="img" aria-label="Porcelain carousel music box">Gifts</div>
<div class="abs tile" style="left:73px;top:873px;width:175px;height:175px;background:linear-gradient(#c9d9c9,#8e9aa8)" role="img" aria-label="Gold earrings with purple stones">Women Earings</div>
<div class="abs tile" style="left:269px;top:691px;width:355px;height:360px;background:radial-gradient(circle at 50% 45%,#d8262a,#a30e14)" role="img" aria-label="Hands passing a wrapped red gift box">Today Best Deal</div>
<div class="abs tile" style="left:633px;top:691px;width:490px;height:360px;background:linear-gradient(110deg,#7f8b94,#c7c1b8 55%,#9aa0a4)" role="img" aria-label="Woman in a santa hat holding a gift">Exclusive Offers</div>
<div class="abs tile" style="left:73px;top:1056px;width:358px;height:176px;background:linear-gradient(#f2f2f2,#b9b9bb)" role="img" aria-label="Illustrated couple print and a printed mug with a rose">Love Gifts</div>
<div class="abs tile" style="left:439px;top:1056px;width:332px;height:176px;background:linear-gradient(#3b3b3b,#141414)" role="img" aria-label="Man in a black tuxedo and bow tie">Mens Clothing</div>
<div class="abs tile" style="left:780px;top:1056px;width:160px;height:176px;background:linear-gradient(#8f8e8b,#6a5a4c)" role="img" aria-label="Brown leather wallet in a gift box">Wallet</div>
<div class="abs tile" style="left:947px;top:1056px;width:176px;height:176px;background:linear-gradient(#a9a6a3,#7b5c42)" role="img" aria-label="Tan leather handbags">Hand Bags</div>

<!-- finding gift for -->
<div class="abs rule" style="left:235px;top:1291px;width:720px"></div>
<h2 class="abs section-title" style="left:0;width:1226px;top:1332px">FINDING GIFT FOR</h2>
<div class="abs gift-for" style="left:71px;background:var(--kids)">KIDS</div>
<div class="abs gift-for" style="left:336px;background:var(--girls)">GIRLS</div>
<div class="abs gift-for" style="left:601px;background:var(--boys)">BOYS</div>
<div class="abs gift-for" style="left:865px;background:var(--other)">OTHER</div>

<!-- top rated -->
<div class="abs rule" style="left:79px;top:1616px;width:486px"></div>
<div class="abs circle-btn sm" style="left:73px;top:1658px"><svg width="10" height="10" viewBox="0 0 10 10"><path d="M6 2L3 5l3 3" stroke="var(--red)" stroke-width="2" fill="none"/></svg></div>
<h2 class="abs section-title" style="left:79px;width:478px;top:1655px">TOP RATED</h2>
<div class="abs circle-btn sm" style="left:537px;top:1658px"><svg width="10" height="10" viewBox="0 0 10 10"><path d="M4 2l3 3-3 3" stroke="var(--red)" stroke-width="2" fill="none"/></svg></div>

<div class="abs" style="left:63px;top:1715px;width:298px;height:333px;background:linear-gradient(120deg,#5a4a40,#1a1a1a 60%)" role="img" aria-label="Man in a tuxedo"><span class="price">$40</span></div>
<div class="abs caption" style="left:63px;top:2060px">Lorem Ipsum is simply dummy text</div>
<div class="abs" style="left:389px;top:1716px;width:172px;height:140px;background:radial-gradient(circle at 60% 45%,#222 0,#111 30%,#8a8a8a 32%,#cfcfcf)" role="img" aria-label="Black eight ball"><span class="price sm">$40</span></div>
<div class="abs caption" style="left:391px;top:1863px">Lorem Ipsum Ipsum...</div>
<div class="abs" style="left:389px;top:1904px;width:172px;height:140px;background:radial-gradient(circle at 60% 45%,#222 0,#111 30%,#8a8a8a 32%,#cfcfcf)" role="img" aria-label="Black eight ball"><span class="price sm">$40</span></div>
<div class="abs caption" style="left:391px;top:2051px">Lorem Ipsum Ipsum...</div>

<!-- recommended -->
<div class="abs rule" style="left:633px;top:1616px;width:488px"></div>
<div class="abs circle-btn sm" style="left:631px;top:1658px"><svg width="10" height="10" viewBox="0 0 10 10"><path d="M6 2L3 5l3 3" stroke="var(--red)" stroke-width="2" fill="none"/></svg></div>
<h2 class="abs section-title" style="left:633px;width:526px;top:1655px">RECOMMENDED</h2>
<div class="abs circle-btn sm" style="left:1095px;top:1658px"><svg width="10" height="10" viewBox="0 0 10 10"><path d="M4 2l3 3-3 3" stroke="var(--red)" stroke-width="2" fill="none"/></svg></div>

<div class="abs" style="left:627px;top:1715px;width:298px;height:333px;background:radial-gradient(circle at 55% 50%,#1e4c66 0,#1e4c66 28%,#b9c0c6 30%,#3c8ac4 55%,#1f5f98)" role="img" aria-label="Steel chronograph wristwatch with a blue dial"><span class="price">$40</span></div>
<div class="abs caption" style="left:627px;top:2060px">Lorem Ipsum is simply dummy text</div>
<div class="abs" style="left:953px;top:1716px;width:172px;height:140px;background:radial-gradient(circle at 60% 45%,#222 0,#111 30%,#8a8a8a 32%,#cfcfcf)" role="img" aria-label="Black eight ball"><span class="price sm">$40</span></div>
<div class="abs caption" style="left:955px;top:1863px">Lorem Ipsum Ipsum...</div>
<div class="abs" style="left:953px;top:1904px;width:172px;height:140px;background:radial-gradient(circle at 60% 45%,#222 0,#111 30%,#8a8a8a 32%,#cfcfcf)" role="img" aria-label="Black eight ball"><span class="price sm">$40</span></div>
<div class="abs caption" style="left:955px;top:2051px">Lorem Ipsum Ipsum...</div>

<!-- snapmira strip -->
<div class="abs strip">
  <div style="width:240px;background:linear-gradient(90deg,#2a78b8,#9fb0bf)" role="img" aria-label="Wristwatch on blue background"></div>
  <div style="width:240px;background:linear-gradient(90deg,#c9c9c9,#222 50%,#bbb)" role="img" aria-label="Black eight ball"></div>
  <div style="width:242px;background:linear-gradient(90deg,#2a78b8,#9fb0bf)" role="img" aria-label="Wristwatch on blue background"></div>
  <div style="width:242px;background:linear-gradient(90deg,#c72a35,#222 60%,#aaa)" role="img" aria-label="Eight ball with playing cards"></div>
  <div style="width:236px;background:linear-gradient(90deg,#ccc,#1a1a1a 40%)" role="img" aria-label="Man in a tuxedo"></div>
</div>
<div class="abs follow-box">
  <h3>FOLLOW<br>US ON<br>SNAPMIRA</h3>
  <div class="follow-btn">FOLLOW <span style="width:18px;height:18px;background:#cfe3f1;border-radius:3px"></span></div>
</div>

<!-- footer -->
<div class="abs foot-h" style="left:75px">About Petal Parcels</div>
<p class="abs about-text">Lorem Ipsum is simply dummy text of the printing and typesetting Lorem Ipsum is simply dummy text printing and typesetting industry<br>Lorem Ipsum is simply dummy text of the printing and typesetting Lorem Ipsum is simply dummy text printing and typesetting industry</p>
<div class="abs about-btn"><span>About Us</span></div>

<div class="abs foot-h" style="left:368px">Quick Links</div>
<ul class="abs foot-list" style="left:368px"><li>Home</li><li>Customer Service</li><li>Site Map</li><li>Orders</li><li>Returns</li><li>Contact Us</li></ul>

<div class="abs foot-h" style="left:576px">Top Categories</div>
<ul class="abs foot-list" style="left:576px"><li>Computers &amp; Tech</li><li>Accessories</li><li>Electronics</li><li>Mobiles &amp;</li><li>Accessories</li><li>Fashion &amp;</li><li>Accessories</li><li>Flowers &amp; Gifts</li></ul>

<div class="abs foot-h" style="left:784px">Follow Us</div>
<ul class="abs social"><li>Chatterleaf</li><li>chirpel</li><li>Linkwell</li><li>clipvane</li><li>Q+</li></ul>

<div class="abs foot-h" style="left:953px">Newsletter</div>
<div class="abs email">Email Address</div>
<div class="abs subscribe">Subscribe</div>

<div class="abs bottom-bar">© Copyright 2015 petalparcels.com | All rights are reserved.</div>

</body>
</html>
```